Verdane Training Center
Golf Simulation & Character Education
Corporate
Milo Raskett
Chief Operations Officer
Brisby Center
North Charleston, SC
Milo@verdanetrainingcenter.com
verdanetrainingcenter.com
I would like for my logo design to be incorporated into the card design
logo full size of card on the back

```html
<!DOCTYPE html>
<html lang="en">
<head>
<meta charset="utf-8">
<title>Verdane Training Center — Business Card</title>
<link rel="stylesheet" href="https://fonts.googleapis.com/css2?family=Open+Sans:wght@400;600;700;800&display=swap">
<style>
  :root {
    --page-bg: #3a3a3c;
    --card-white: #ffffff;
    --red-light: #c2272d;
    --red-mid: #9e1b20;
    --red-dark: #5e0c10;
    --stripe-black: #141414;
    --text-light: #ffffff;
    --brand-red: #b01e24;
  }
  html, body {
    margin: 0;
    padding: 0;
    width: 1200px;
    height: 878px;
    overflow: hidden;
    background: var(--page-bg);
    font-family: "Open Sans", sans-serif;
  }
  .business-card {
    position: absolute;
    left: 110px;
    top: 159px;
    width: 980px;
    height: 560px;
    border-radius: 30px;
    overflow: hidden;
    background: var(--card-white);
  }
  .card-art {
    position: absolute;
    inset: 0;
  }
  .brand-block {
    position: absolute;
    left: 60px;
    top: 222px;
    width: 330px;
    display: flex;
    align-items: center;
    gap: 14px;
  }
  .brand-dot {
    flex: none;
    width: 34px;
    height: 34px;
    border-radius: 50%;
    background: var(--brand-red);
  }
  .brand-name {
    font-weight: 800;
    font-size: 34px;
    line-height: 1.08;
    color: var(--brand-red);
    letter-spacing: 0.5px;
  }
  .contact-block {
    position: absolute;
    right: 44px;
    top: 0;
    bottom: 0;
    width: 460px;
    color: var(--text-light);
    text-align: right;
  }
  .person-name {
    position: absolute;
    right: 0;
    top: 40px;
    margin: 0;
    font-weight: 700;
    font-size: 40px;
    line-height: 1;
  }
  .person-title {
    position: absolute;
    right: 0;
    top: 88px;
    margin: 0;
    font-weight: 600;
    font-size: 23px;
  }
  .address {
    position: absolute;
    right: 52px;
    top: 232px;
    margin: 0;
    font-style: normal;
    font-size: 24px;
    line-height: 1.32;
  }
  .contact-line {
    position: absolute;
    right: 0;
    display: flex;
    align-items: center;
    gap: 14px;
    font-size: 23px;
  }
  .contact-line svg { width: 26px; height: 26px; flex: none; }
  .line-phone { top: 380px; }
  .line-email { top: 432px; }
  .line-web { top: 474px; }
</style>
</head>
<body>
  <div class="business-card">
    <svg class="card-art" viewBox="0 0 980 560" width="980" height="560" aria-hidden="true">
      <defs>
        <radialGradient id="redGlow" cx="0.55" cy="0.48" r="0.65">
          <stop offset="0" stop-color="var(--red-light)"/>
          <stop offset="0.55" stop-color="var(--red-mid)"/>
          <stop offset="1" stop-color="var(--red-dark)"/>
        </radialGradient>
      </defs>
      <path d="M470 0 C380 150 380 400 500 560 L980 560 L980 0 Z" fill="url(#redGlow)"/>
      <path d="M470 0 C380 150 380 400 500 560 L520 560 C410 400 410 160 500 0 Z" fill="var(--stripe-black)"/>
    </svg>

    <div class="brand-block">
      <span class="brand-dot"></span>
      <span class="brand-name">Verdane<br>Training Center</span>
    </div>

    <div class="contact-block">
      <h1 class="person-name">Milo Raskett</h1>
      <p class="person-title">Chief Operations Officer</p>
      <address class="address">Brisby Center<br>Fenwick Bay,<br>SC 29912</address>
      <div class="contact-line line-phone">
        <span>843-555-0142</span>
        <svg viewBox="0 0 24 24" aria-hidden="true"><rect x="7" y="2" width="10" height="20" rx="2" fill="none" stroke="#fff" stroke-width="2"/><circle cx="12" cy="18" r="1.3" fill="#fff"/></svg>
      </div>
      <div class="contact-line line-email">
        <span>Milo@verdanetrainingcenter.com</span>
        <svg viewBox="0 0 24 24" aria-hidden="true"><circle cx="12" cy="12" r="4" fill="none" stroke="#fff" stroke-width="2"/><path d="M16 8v5.5a2.5 2.5 0 0 0 5 0V12a9 9 0 1 0-4 7.5" fill="none" stroke="#fff" stroke-width="2"/></svg>
      </div>
      <div class="contact-line line-web">
        <span>www.verdanetrainingcenter.com</span>
        <svg viewBox="0 0 24 24" aria-hidden="true"><circle cx="12" cy="12" r="9" fill="none" stroke="#fff" stroke-width="2"/><ellipse cx="12" cy="12" rx="4" ry="9" fill="none" stroke="#fff" stroke-width="1.6"/><path d="M3 12h18M5 7h14M5 17h14" stroke="#fff" stroke-width="1.4"/></svg>
      </div>
    </div>
  </div>
</body>
</html>
```